Garden Maintenance business card

I need a business card design for my new business "Corrowong Garden Crew". I do garden maintenance including lawns, turf lawn, pruning, hedging, water systems, anything related to the garden really (dont think i need to include any of that except garden maintenance)

Reason: narrowed it down and just showing my business partners the designs, cheers

Industry/Entity Type

Business

Requirements
Must have
• Must Have:
- ABN: XX XXX XXX XXX
Mobile phone number 00 0000000
email address xxxx.xxxxxx@gmail.com
Owner Name Xxxx xxxxxx
title: garden specialist possibly under name or something sounding professional
logo which has been submitted both with a background and one without, feel free to choose whichever one you like
business name

```html
<!DOCTYPE html>
<html lang="en">
<head>
<meta charset="utf-8">
<title>Corrowong Garden Crew – Business Card</title>
<link rel="stylesheet" href="https://fonts.googleapis.com/css2?family=Questrial&family=Arimo:wght@400&display=swap">
<style>
  :root {
    --page-bg: #ecebe8;
    --card-bg: #f7f6f3;
    --brand-green: #6dbd4f;
    --tagline-grey: #7b7b7b;
    --body-ink: #2e2e2e;
    --mark-green: #c9dfb8;
    --card-shadow: rgba(0, 0, 0, 0.18);
  }
  * { box-sizing: border-box; margin: 0; padding: 0; }
  html, body {
    width: 1200px;
    height: 1000px;
    overflow: hidden;
    background: var(--page-bg);
  }
  .canvas {
    position: relative;
    width: 1200px;
    height: 1000px;
  }
  .card {
    position: absolute;
    left: 267px;
    width: 651px;
    height: 372px;
    background: var(--card-bg);
    border-radius: 22px;
    box-shadow: 0 3px 10px var(--card-shadow);
    overflow: hidden;
  }
  .card--front { top: 92px; }
  .card--back { top: 532px; }

  .brand-name {
    position: absolute;
    left: 0;
    right: 0;
    text-align: center;
    font-family: "Questrial", sans-serif;
    color: var(--brand-green);
    white-space: nowrap;
  }
  .tagline {
    position: absolute;
    left: 0;
    right: 0;
    text-align: center;
    font-family: "Arimo", sans-serif;
    color: var(--tagline-grey);
    text-transform: uppercase;
    white-space: nowrap;
  }

  /* Front */
  .card--front .logo-mark {
    position: absolute;
    left: 275px;
    top: 70px;
    width: 140px;
    height: 140px;
  }
  .card--front .brand-name {
    top: 282px;
    font-size: 26px;
    letter-spacing: -0.2px;
    padding-left: 4px;
  }
  .card--front .tagline {
    top: 316px;
    font-size: 13px;
    letter-spacing: 4.2px;
    padding-left: 4px;
  }

  /* Back */
  .card--back .brand-name {
    top: 44px;
    font-size: 40px;
    letter-spacing: -0.3px;
    padding-left: 4px;
  }
  .card--back .tagline {
    top: 94px;
    font-size: 20px;
    letter-spacing: 6.2px;
    padding-left: 6px;
  }
  .contact-list {
    position: absolute;
    left: 229px;
    top: 180px;
    list-style: none;
    font-family: "Arimo", sans-serif;
    font-size: 16px;
    color: var(--body-ink);
    line-height: 34px;
  }
  .card--back .logo-mark {
    position: absolute;
    left: 544px;
    top: 218px;
    width: 62px;
    height: 62px;
  }
</style>
</head>
<body>
<main class="canvas">

  <section class="card card--front" aria-label="Business card front">
    <svg class="logo-mark" viewBox="0 0 140 140" aria-hidden="true">
      <circle cx="70" cy="70" r="70" fill="var(--mark-green)"/>
    </svg>
    <h1 class="brand-name">Corrowong Garden Crew</h1>
    <p class="tagline">Garden Specialist</p>
  </section>

  <section class="card card--back" aria-label="Business card back">
    <h2 class="brand-name">Corrowong Garden Crew</h2>
    <p class="tagline">Garden Specialist</p>
    <ul class="contact-list">
      <li>ABN: XX XXX XXX XXX</li>
      <li>Mobile phone number: 00 0000000</li>
      <li>Email address: xxxx.xxxxxx@gmail.com</li>
      <li>Owner Name: Xxxx xxxxxx</li>
    </ul>
    <svg class="logo-mark" viewBox="0 0 62 62" aria-hidden="true">
      <circle cx="31" cy="31" r="31" fill="var(--mark-green)"/>
    </svg>
  </section>

</main>
</body>
</html>
```